Brightwire Hollow Business cards

one side I would like my logo (uploaded) and the other side I want my details. I'm an electrician in sydney. The logo side I'm happy with just a white background and our logo in the middle.

Details for other side
24/7 Sydney Electrician
Marcus Pell
0431 587 219
marcus@brightwirehollow.com.au
brightwirehollow.com.au
icons for facebook, instagram, linked in

Industry/Entity Type

electrician

Contact Information for Business Card

company info

```html
<!DOCTYPE html>
<html lang="en">
<head>
<meta charset="utf-8">
<title>Brightwire Hollow – Business Cards</title>
<link rel="stylesheet" href="https://fonts.googleapis.com/css2?family=Rubik:wght@500;700;800&display=swap">
<style>
  :root {
    --backdrop: #2b2d2f;
    --card-white: #ffffff;
    --card-black: #0d0d0d;
    --brand-red: #f2281c;
    --ink-white: #ffffff;
    --ink-black: #111111;
  }
  * { margin: 0; padding: 0; box-sizing: border-box; }
  html, body { width: 1200px; height: 939px; overflow: hidden; }
  body {
    background: var(--backdrop);
    font-family: "Rubik", sans-serif;
    position: relative;
  }
  .card {
    position: absolute;
    width: 560px;
    height: 320px;
    box-shadow: 0 14px 30px rgba(0,0,0,.45);
  }
  .card--front { left: 100px; top: 110px; background: var(--card-white); }
  .card--back  { left: 540px; top: 500px; background: var(--card-black); overflow: hidden; }

  .brand-name {
    color: var(--brand-red);
    font-weight: 800;
    text-transform: uppercase;
    line-height: 1;
    letter-spacing: 2px;
  }
  .card--front .brand-name {
    position: absolute; left: 0; right: 0; top: 100px;
    text-align: center; font-size: 40px;
  }
  .social-row {
    position: absolute; left: 0; right: 0; top: 238px;
    display: flex; justify-content: center; gap: 8px;
  }
  .social-dot {
    width: 30px; height: 30px; border-radius: 50%;
    background: var(--brand-red);
  }

  .card--back .brand-name {
    position: absolute; left: 40px; width: 210px; top: 98px;
    text-align: center; font-size: 30px;
  }
  .divider {
    position: absolute; left: 268px; top: 66px;
    width: 2px; height: 118px; background: var(--ink-white);
  }
  .contact-block { position: absolute; left: 296px; top: 70px; }
  .contact-name {
    color: var(--brand-red); font-weight: 800; font-size: 26px;
    text-transform: uppercase; letter-spacing: .5px; margin-bottom: 10px;
  }
  .contact-line {
    display: flex; align-items: center; gap: 8px;
    color: var(--ink-white); font-size: 12.5px; font-weight: 500;
    margin-bottom: 7px;
  }
  .contact-line--phone { font-weight: 700; font-size: 15px; letter-spacing: .5px; }
  .contact-icon { width: 13px; height: 13px; flex: none; }
  .tagline-band { position: absolute; left: 0; top: 240px; width: 560px; height: 60px; }
  .tagline {
    position: absolute; left: 150px; width: 270px; top: 258px;
    text-align: center; color: var(--ink-white);
    font-weight: 700; font-size: 12px; letter-spacing: 4px; text-transform: uppercase;
  }
</style>
</head>
<body>

<section class="card card--front" aria-label="Business card front">
  <div class="brand-name">Brightwire<br>Hollow</div>
  <div class="social-row">
    <span class="social-dot" role="img" aria-label="Social media link"></span>
    <span class="social-dot" role="img" aria-label="Social media link"></span>
  </div>
</section>

<section class="card card--back" aria-label="Business card back">
  <div class="brand-name">Brightwire<br>Hollow</div>
  <div class="divider"></div>

  <div class="contact-block">
    <div class="contact-name">Marcus Pell</div>
    <div class="contact-line contact-line--phone">
      <svg class="contact-icon" viewBox="0 0 16 16" aria-hidden="true"><path fill="#f2281c" d="M3.5 1.5l2.5 0 1 3.5-1.6 1.2c.8 1.7 2.2 3.1 3.9 3.9L10.5 8.5 14 9.5v2.5c0 1-1 2-2 2C6.5 14 2 9.5 2 3.5c0-1 .8-2 1.5-2z"/></svg>
      0431 587 219
    </div>
    <div class="contact-line">
      <svg class="contact-icon" viewBox="0 0 16 16" aria-hidden="true"><rect x="1" y="3" width="14" height="10" fill="#f2281c"/><path d="M1 3.5l7 5 7-5" fill="none" stroke="#0d0d0d" stroke-width="1.4"/></svg>
      marcus@brightwirehollow.com.au
    </div>
    <div class="contact-line">
      <svg class="contact-icon" viewBox="0 0 16 16" aria-hidden="true"><circle cx="8" cy="8" r="7" fill="#f2281c"/><path d="M1 8h14M8 1c-3 3.5-3 10.5 0 14M8 1c3 3.5 3 10.5 0 14" fill="none" stroke="#0d0d0d" stroke-width="1.1"/></svg>
      brightwirehollow.com.au
    </div>
  </div>

  <svg class="tagline-band" viewBox="0 0 560 60" aria-hidden="true">
    <path fill="#f2281c" d="M0 40h140v-30h290v-10h130v6h-124v32h-290v10h-146z"/>
    <rect x="140" y="10" width="290" height="28" fill="#f2281c"/>
  </svg>
  <div class="tagline">24/7 Sydney Electricians</div>
</section>

</body>
</html>
```